Copperleaf Vantage Training PowerPoint Template

I want to PowerPoint template theme using my attached logo. My colors are black and orange. My website is CopperleafVantage.com. I am a handgun training company.

Font:

- Serpentine-Bold-Bold for "IRON BRAE"

- BrowalliaUPC for "SHOOTING SPORTS"

Colors (CMYK code):

- BLACK ....... 0; 0; 0; 100;
- ORANGE ... gradient from 0; 65; 97.5; 0 to 0; 39; 97.5; 0

```html
<!DOCTYPE html>
<html lang="en">
<head>
<meta charset="utf-8">
<title>Copperleaf Vantage Training – Slide Templates</title>
<link href="https://fonts.googleapis.com/css2?family=Arimo:ital,wght@0,400;0,700;1,700&family=Orbitron:wght@900&display=swap" rel="stylesheet">
<style>
  :root {
    --sheet-bg: #9aa68a;
    --black: #000000;
    --panel-black: #0d0d0d;
    --orange-deep: #e07f1c;
    --orange-light: #f0b400;
    --title-yellow: #f2b705;
    --white: #ffffff;
    --steel: #8a8a8a;
    --body-cream: #fde7b0;
    --ink: #151515;
  }
  * { margin: 0; padding: 0; box-sizing: border-box; }
  html, body { width: 810px; height: 1200px; overflow: hidden; }
  body {
    position: relative;
    background: var(--sheet-bg);
    font-family: "Arimo", Arial, sans-serif;
  }
  .sheet-label {
    position: absolute; left: 0; width: 810px; text-align: center;
    color: var(--white); font-size: 38px; line-height: 1;
    text-shadow: 1px 2px 3px rgba(0,0,0,.55);
  }
  .sheet-label.main { top: 8px; }
  .sheet-label.secondary { top: 590px; }

  .slide { position: absolute; left: 60px; width: 690px; overflow: hidden; }

  /* Title slide */
  .title-slide { top: 53px; height: 519px; background: var(--panel-black); }
  .title-slide .header {
    position: absolute; left: 0; top: 0; width: 690px; height: 105px;
    background: linear-gradient(90deg, var(--orange-deep), var(--orange-light) 50%, var(--orange-deep));
    border-bottom: 3px solid var(--steel);
  }
  .brand-mark { position: absolute; display: flex; align-items: center; gap: 6px; }
  .brand-mark .dot { width: 16px; height: 16px; border-radius: 50%; flex: none; }
  .brand-mark .name { font-weight: 700; font-size: 12px; line-height: 1.1; text-transform: uppercase; }
  .header .brand-mark { left: 16px; top: 36px; }
  .header .brand-mark .dot { background: var(--black); }
  .header .brand-mark .name { color: var(--black); }
  .header .wordmark {
    position: absolute; left: 140px; top: 24px; width: 540px; text-align: center;
    font-size: 26px; color: var(--black); letter-spacing: .5px; white-space: nowrap;
  }
  .wordmark b { font-weight: 700; }
  .header .site-url {
    position: absolute; left: 140px; top: 63px; width: 540px; text-align: center;
    font-size: 16px; color: var(--black);
  }
  .title-slide .stage {
    position: absolute; left: 0; top: 108px; width: 690px; height: 371px;
    background-color: var(--panel-black);
    background-image: radial-gradient(rgba(255,255,255,.05) 1px, transparent 1.4px);
    background-size: 5px 5px;
  }
  .presentation-title {
    position: absolute; left: 0; top: 232px; width: 690px; text-align: center;
    font-family: "Orbitron", "Arial Black", sans-serif; font-weight: 900;
    font-size: 38px; color: var(--title-yellow); letter-spacing: 1px;
  }
  .presentation-subtitle {
    position: absolute; left: 0; top: 313px; width: 690px; text-align: center;
    font-size: 24px; color: var(--white);
  }
  .title-slide .footer {
    position: absolute; left: 0; top: 479px; width: 690px; height: 40px;
    border-top: 4px solid var(--orange-deep); background: var(--black);
    color: var(--white); font-size: 16px;
  }
  .footer .date { position: absolute; left: 13px; top: 10px; }
  .footer .presenter { position: absolute; left: 0; width: 690px; top: 10px; text-align: center; font-weight: 700; }
  .footer .job-title { position: absolute; right: 12px; top: 10px; }

  /* Content slide */
  .content-slide {
    top: 637px; height: 518px;
    background: linear-gradient(180deg, var(--white) 0%, var(--white) 45%, var(--body-cream) 100%);
  }
  .content-slide .title-bar { position: absolute; left: 0; top: 0; width: 690px; height: 65px; background: var(--black); }
  .title-bar svg { position: absolute; left: 0; top: 0; }
  .slide-heading {
    position: absolute; left: 24px; top: 19px;
    font-family: "Orbitron", "Arial Black", sans-serif; font-weight: 900;
    font-size: 20px; color: var(--white); letter-spacing: .5px;
  }
  .rules { position: absolute; left: 48px; top: 150px; width: 440px; list-style: none; }
  .rules li {
    position: relative; padding-left: 43px; margin-bottom: 16px;
    font-weight: 700; font-style: italic; font-size: 17px; line-height: 28px; color: var(--ink);
  }
  .rules li svg { position: absolute; left: 2px; top: 4px; }
  .illustration {
    position: absolute; left: 478px; top: 112px; width: 172px; height: 262px;
    background: linear-gradient(160deg, #2a2a2a, #8c8c8c 60%, #e6e6e6);
    border-radius: 10px;
  }
  .content-slide .footer { position: absolute; left: 0; top: 471px; width: 690px; height: 47px; }
  .content-slide .footer svg { position: absolute; left: 0; top: 0; }
  .content-slide .footer .brand-mark { left: 12px; top: 14px; }
  .content-slide .footer .brand-mark .dot { background: var(--orange-light); }
  .content-slide .footer .brand-mark .name { color: var(--white); font-size: 9px; }
  .content-slide .footer .wordmark {
    position: absolute; left: 100px; top: 12px; font-size: 19px; color: var(--white); white-space: nowrap;
  }
  .slide-number {
    position: absolute; right: 22px; top: 8px; font-weight: 700; font-size: 28px; color: var(--white);
  }
</style>
</head>
<body>
  <div class="sheet-label main">Main Template</div>

  <section class="slide title-slide">
    <header class="header">
      <div class="brand-mark"><span class="dot"></span><span class="name">Copperleaf<br>Vantage</span></div>
      <div class="wordmark"><b>COPPERLEAF</b> VANTAGE TRAINING</div>
      <div class="site-url">www.copperleafvantage.com</div>
    </header>
    <div class="stage"></div>
    <h1 class="presentation-title">PRESENTATION TITLE</h1>
    <p class="presentation-subtitle">Presentation Subtitle</p>
    <footer class="footer">
      <span class="date">16 February 2014</span>
      <span class="presenter">PRESENTOR’S NAME</span>
      <span class="job-title">Job Title</span>
    </footer>
  </section>

  <div class="sheet-label secondary">Secondary Template</div>

  <section class="slide content-slide">
    <div class="title-bar">
      <svg width="690" height="65" viewBox="0 0 690 65">
        <defs>
          <linearGradient id="bar-orange" x1="0" x2="1" y1="0" y2="0">
            <stop offset="0" stop-color="#e07f1c"/>
            <stop offset="1" stop-color="#f0b400"/>
          </linearGradient>
        </defs>
        <polygon points="12,13 537,13 565,53 12,53" fill="url(#bar-orange)"/>
      </svg>
      <h2 class="slide-heading">THE 4 GUN SAFETY RULES</h2>
    </div>

    <ul class="rules">
      <li><svg width="22" height="22" viewBox="0 0 22 22"><circle cx="11" cy="11" r="10" fill="#c9c9c9"/><circle cx="11" cy="11" r="5" fill="#333"/></svg>All guns are ALWAYS loaded</li>
      <li><svg width="22" height="22" viewBox="0 0 22 22"><circle cx="11" cy="11" r="10" fill="#c9c9c9"/><circle cx="11" cy="11" r="5" fill="#333"/></svg>ALWAYS keep your finger off the trigger until ready to shoot.</li>
      <li><svg width="22" height="22" viewBox="0 0 22 22"><circle cx="11" cy="11" r="10" fill="#c9c9c9"/><circle cx="11" cy="11" r="5" fill="#333"/></svg>NEVER point the gun at anything you are not willing to destroy.</li>
      <li><svg width="22" height="22" viewBox="0 0 22 22"><circle cx="11" cy="11" r="10" fill="#c9c9c9"/><circle cx="11" cy="11" r="5" fill="#333"/></svg>ALWAYS know your target and what is beyond.</li>
    </ul>

    <div class="illustration" role="img" aria-label="Black and white illustration of a hand holding a revolver pointed toward the viewer"></div>

    <footer class="footer">
      <svg width="690" height="47" viewBox="0 0 690 47">
        <defs>
          <linearGradient id="num-orange" x1="0" x2="1" y1="0" y2="0">
            <stop offset="0" stop-color="#f0b400"/>
            <stop offset="1" stop-color="#e07f1c"/>
          </linearGradient>
        </defs>
        <rect x="0" y="0" width="690" height="47" fill="#000"/>
        <rect x="0" y="0" width="600" height="3" fill="#e07f1c"/>
        <polygon points="578,0 690,0 690,47 612,47" fill="url(#num-orange)"/>
      </svg>
      <div class="brand-mark"><span class="dot"></span><span class="name">Copperleaf<br>Vantage</span></div>
      <div class="wordmark"><b>COPPERLEAF</b> VANTAGE TRAINING</div>
      <span class="slide-number">01</span>
    </footer>
  </section>
</body>
</html>
```